WinterCommuters

First, let me apologize for the short term. We just got an opportunity to place an ad in a commuter newspaper that will run throughout the winter months. We have tropical vacation rentals in Mexico, so it seems worth a shot.

We want to emphasize tropical luxury at competitive prices. Because we will be new to the audience, we need to cover a lot in one ad - images can definitely help. We are supplying photographs - feel free to crop or whatever.

We have the only private complex of luxury houses on the Mexican Caribbean coast, the "Riviera Maya" so we can accommodate anywhere from a single couple to a full wedding party. We want to show our large capacity without scaring off the single couple or small family with mom, dad, and a couple of kids.
Updates

Correction to text:  third paragraph.  The word should be "you", not "so" after "Riviera Maya,"
"As we are in the heart of the Riviera Maya, you will have "

Target Market(s)

Professionals looking to get out of the winter cold. Think tropical!

Industry/Entity Type

Wedding

Requirements
Must have
• The ad must be 5"x5" at 200 DPI (1,000 x 1000 pixels).
• The primary ad will be printed in black and white so it should be saved as a grayscale image. (I think they actually want a jpg, although a tiff would seem more logical!)
• The add will also be on the web in full color so please design the ad with color in mind and then change to grayscale after the content ends.
• Include our logo, phone number, e-mail, and website.
• Also, unless there is a good reason not to, include the four "first tier" images.
• Use the text as provided - not that some is optional.
Nice to have
• Please see the text in the attachments. OOPS: I downloaded the wrong version first - use the most recent "chicagoad" text!
• Also, unless there is a strong reason, use the "first tier" photos. We want to emphasize the accommodations, but also show large groups. We don't want to scare off the smaller groups (couples, small families) with the impression that we are only for large groups.
• The "second tier" photos are available if they would help. Both accommodation and weddings/large groups.
Should not have
• Stock photographs.
• I have (obviously) had some issues loading my files so please forgive the duplicates.

```html
<!DOCTYPE html>
<html lang="en">
<head>
<meta charset="utf-8">
<title>Casa Tortuga – Winter Commuter Ad</title>
<link href="https://fonts.googleapis.com/css2?family=Sriracha&family=Open+Sans:wght@400;600;700&display=swap" rel="stylesheet">
<style>
  :root{
    --royal:#4a5fb5;
    --royal-dark:#3a4c9c;
    --teal:#2fb8c4;
    --sun:#f2e33a;
    --orange:#f08a2c;
    --ink:#1d1d1d;
    --paper:#ffffff;
    --cream:#fbf6dc;
    --frame:#ffffff;
    --sea:#5fa9c9;
    --sunset:#e6a24a;
    --sand:#d8b25c;
    --villa:#b98a5e;
  }
  *{box-sizing:border-box;margin:0;padding:0}
  html,body{width:1200px;height:584px;overflow:hidden;background:#fff}
  .sheet{position:relative;width:1200px;height:584px}
  .ad{position:absolute;top:0;width:590px;height:584px;overflow:hidden;
      border:3px solid var(--royal);
      background:radial-gradient(ellipse at 95% 0%,var(--cream) 0%,var(--paper) 45%);}
  .ad--color{left:0}
  .ad--grayscale{left:610px;filter:grayscale(1)}
  .side-column{position:absolute;left:0;top:0;width:150px;height:100%;
      background:linear-gradient(180deg,var(--royal) 0%,var(--royal-dark) 100%)}
  .curve-band{position:absolute;left:0;top:0;width:220px;height:584px}
  .tagline{position:absolute;left:134px;top:12px;height:540px;width:40px;
      writing-mode:vertical-rl;transform:rotate(180deg);
      font-family:"Sriracha",cursive;font-size:23px;color:var(--paper);
      text-align:center;line-height:40px;letter-spacing:.3px;white-space:nowrap}
  .stamp{position:absolute;left:10px;width:118px;height:112px;background:var(--frame);
      padding:6px;border:2px dotted #cfd6f0}
  .stamp .photo{width:100%;height:100%}
  .stamp--vacation{top:4px}  .stamp--vacation .photo{background:linear-gradient(180deg,#9fd3f0 0%,var(--sea) 55%,#2d7d8d 100%)}
  .stamp--wedding{top:144px} .stamp--wedding .photo{background:linear-gradient(180deg,#f3c574 0%,var(--sunset) 50%,#4b3a2a 100%)}
  .stamp--reunion{top:280px} .stamp--reunion .photo{background:radial-gradient(circle,#efe2b8 0%,var(--sand) 60%,#a98a4e 100%)}
  .stamp--retreat{top:416px} .stamp--retreat .photo{background:linear-gradient(180deg,#8fc1e6 0%,var(--villa) 55%,#6f7b4a 100%)}
  .stamp-label{position:absolute;left:14px;font-family:"Sriracha",cursive;font-size:21px;color:var(--sun);line-height:1;white-space:nowrap}
  .label--vacation{top:118px} .label--wedding{top:254px} .label--reunion{top:389px} .label--retreat{top:526px}
  .headline{position:absolute;left:196px;top:12px;font-family:"Sriracha",cursive;font-weight:400;
      font-size:24px;line-height:31px;color:var(--royal);white-space:nowrap;letter-spacing:-.2px}
  .headline span{display:block}
  .headline span:nth-child(2){padding-left:6px}
  .headline span:nth-child(3){padding-left:10px}
  .body-copy{position:absolute;left:213px;top:113px;width:348px;
      font-family:"Open Sans",sans-serif;font-size:11.3px;line-height:19px;color:var(--ink)}
  .body-copy p{margin:0}
  .body-copy p+p{margin-top:1px}
  .questions{position:absolute;left:200px;top:292px;width:385px;
      font-family:"Open Sans",sans-serif;font-weight:700;font-size:15.2px;line-height:19px;color:var(--orange);white-space:nowrap}
  .questions p{margin-bottom:4px}
  .questions p:nth-child(2){padding-left:3px}
  .capacity{position:absolute;left:186px;top:412px;font-family:"Open Sans",sans-serif;
      font-weight:700;font-size:16.3px;line-height:22px;color:var(--royal);white-space:nowrap}
  .invite{position:absolute;left:188px;top:462px;font-family:"Open Sans",sans-serif;
      font-weight:600;font-size:13.2px;line-height:20.5px;color:var(--ink);white-space:nowrap}
  .brand-disc{position:absolute;left:452px;top:424px;width:132px;height:132px;border-radius:50%;
      background:var(--teal);display:flex;align-items:center;justify-content:center}
  .brand-name{font-family:"Open Sans",sans-serif;font-weight:700;font-size:17px;color:var(--paper);
      text-align:center;line-height:20px}
  .footer{position:absolute;left:0;bottom:0;width:100%;height:30px;background:var(--royal);
      display:flex;align-items:center;justify-content:space-evenly;white-space:nowrap;
      font-family:"Sriracha",cursive;font-size:14px;color:var(--paper);padding:0 6px}
  .ad--grayscale .questions,.ad--grayscale .capacity{color:var(--ink)}
</style>
</head>
<body>
<main class="sheet">

  <section class="ad ad--color" aria-label="Casa Tortuga advertisement, colour version">
    <div class="side-column"></div>
    <svg class="curve-band" viewBox="0 0 220 584" aria-hidden="true">
      <path d="M140 0 C150 120 125 300 132 430 C136 500 130 560 140 584 L180 584 C172 540 178 470 176 420 C170 300 200 140 185 0 Z" fill="var(--teal)"/>
    </svg>
    <div class="tagline">Wouldn't you rather be in a tropical paradise?</div>

    <div class="stamp stamp--vacation"><div class="photo" role="img" aria-label="Pool at the edge of the sea, with palm trees"></div></div>
    <div class="stamp-label label--vacation">Vacations</div>
    <div class="stamp stamp--wedding"><div class="photo" role="img" aria-label="Bride on the beach at sunset"></div></div>
    <div class="stamp-label label--wedding">Weddings</div>
    <div class="stamp stamp--reunion"><div class="photo" role="img" aria-label="Round banquet table set for a group, seen from above"></div></div>
    <div class="stamp-label label--reunion">Reunions</div>
    <div class="stamp stamp--retreat"><div class="photo" role="img" aria-label="Courtyard of a luxury villa with a tower"></div></div>
    <div class="stamp-label label--retreat">Retreats</div>

    <h1 class="headline"><span>Come and relax in the only</span><span>private complex of luxury houses</span><span>on the beautiful Mexican Riviera.</span></h1>

    <div class="body-copy">
      <p>Only 60 miles South of Cancun, we are a world apart from the noise and crowds of large hotels and party towns.</p>
      <p>Located in the quiet coastal village of Akumal, you get all of the best amenities, great restaurants, magnificent snorkeling and diving, beaches, and more in the laid back autmosphere that is so hard to find.</p>
      <p>As we are in the heart of the Riviera Maya, you will have access to shopping, Mayan ruins, tourist attractions, golf, sailing, diving and much more.</p>
    </div>

    <div class="questions">
      <p>Are you a couple looking for that perfect,<br>secluded getaway?</p>
      <p>Are you looking for a vacation in a quiet,<br>safe, family-friendly area?</p>
      <p>Are you looking to all be together for a wedding,<br>family reunion, or retreat?</p>
    </div>

    <p class="capacity">With 5 luxury homes to choose from,<br>we can meet your exact needs.</p>

    <p class="invite">Visit our web site or call us directly.<br>We look forward to hearing from<br>you and to sharing our homes with<br>you, your family and friends.</p>

    <div class="brand-disc"><span class="brand-name">Casa<br>Tortuga</span></div>

    <footer class="footer">
      <span>Daniel &amp; Nora Vale</span><span>•</span><span>(555) 214-0388</span><span>•</span><span>hello@CasaTortuga.com</span><span>•</span><span>www.CasaTortuga.com</span>
    </footer>
  </section>

  <section class="ad ad--grayscale" aria-label="Casa Tortuga advertisement, grayscale print version">
    <div class="side-column"></div>
    <svg class="curve-band" viewBox="0 0 220 584" aria-hidden="true">
      <path d="M140 0 C150 120 125 300 132 430 C136 500 130 560 140 584 L180 584 C172 540 178 470 176 420 C170 300 200 140 185 0 Z" fill="var(--teal)"/>
    </svg>
    <div class="tagline">Wouldn't you rather be in a tropical paradise?</div>

    <div class="stamp stamp--vacation"><div class="photo" role="img" aria-label="Pool at the edge of the sea, with palm trees"></div></div>
    <div class="stamp-label label--vacation">Vacations</div>
    <div class="stamp stamp--wedding"><div class="photo" role="img" aria-label="Bride on the beach at sunset"></div></div>
    <div class="stamp-label label--wedding">Weddings</div>
    <div class="stamp stamp--reunion"><div class="photo" role="img" aria-label="Round banquet table set for a group, seen from above"></div></div>
    <div class="stamp-label label--reunion">Reunions</div>
    <div class="stamp stamp--retreat"><div class="photo" role="img" aria-label="Courtyard of a luxury villa with a tower"></div></div>
    <div class="stamp-label label--retreat">Retreats</div>

    <h2 class="headline"><span>Come and relax in the only</span><span>private complex of luxury houses</span><span>on the beautiful Mexican Riviera.</span></h2>

    <div class="body-copy">
      <p>Only 60 miles South of Cancun, we are a world apart from the noise and crowds of large hotels and party towns.</p>
      <p>Located in the quiet coastal village of Akumal, you get all of the best amenities, great restaurants, magnificent snorkeling and diving, beaches, and more in the laid back autmosphere that is so hard to find.</p>
      <p>As we are in the heart of the Riviera Maya, you will have access to shopping, Mayan ruins, tourist attractions, golf, sailing, diving and much more.</p>
    </div>

    <div class="questions">
      <p>Are you a couple looking for that perfect,<br>secluded getaway?</p>
      <p>Are you looking for a vacation in a quiet,<br>safe, family-friendly area?</p>
      <p>Are you looking to all be together for a wedding,<br>family reunion, or retreat?</p>
    </div>

    <p class="capacity">With 5 luxury homes to choose from,<br>we can meet your exact needs.</p>

    <p class="invite">Visit our web site or call us directly.<br>We look forward to hearing from<br>you and to sharing our homes with<br>you, your family and friends.</p>

    <div class="brand-disc"><span class="brand-name">Casa<br>Tortuga</span></div>

    <footer class="footer">
      <span>Daniel &amp; Nora Vale</span><span>•</span><span>(555) 214-0388</span><span>•</span><span>hello@CasaTortuga.com</span><span>•</span><span>www.CasaTortuga.com</span>
    </footer>
  </section>

</main>
</body>
</html>
```